Retractable Banner Design for a GRC Software Product in Healthcare domain

We want a banner for branding and product positioning, in conferences and stalls. The stall's objective is to generate interest in the product, understand the market better, get feedback on the offering and to create customer engagements.

The banner should encourage visitors to drop by our stalls seeking more information about our product offering.

Target Market(s)

Asia

Industry/Entity Type

Healthcare

Requirements
Must have
• Product Logo, Tagline - "Patient Safety Solutions For Every Hospital", Visual indicators for Secure Software, Ease of use and Mobile responsive nature, Indicate availability of two flagship modules - Beacon Desk and Larkspur Summit Console
• QR Code link to the website.
Nice to have
• Module 1-line descriptions:
• Beacon Desk: Make Incident reporting easy, meaningful and secure.
• Larkspur Summit Console: Driver quality improvement efforts in healthcare.
• Relevant background pictures and/or graphics. We can provide 2-3 charts and/or screenshots if they would be more meaningful.
Should not have
• Should not be verbose.

```html
<!DOCTYPE html>
<html lang="en">
<head>
<meta charset="utf-8">
<title>Verital – Patient Safety Banner</title>
<link href="https://fonts.googleapis.com/css2?family=Montserrat:wght@400;500;600;700;800&display=swap" rel="stylesheet">
<style>
  :root {
    --green: #1b6f35;
    --green-bright: #12973f;
    --red: #e0221f;
    --ink: #151515;
    --white: #ffffff;
    --stage: #e4e5e7;
    --photo-dark: #3c4a52;
    --photo-mid: #8c9aa3;
    --photo-light: #d8dde0;
  }
  * { box-sizing: border-box; margin: 0; padding: 0; }
  html, body { width: 1094px; height: 1200px; overflow: hidden; }
  body { background: var(--stage); font-family: "Montserrat", sans-serif; }

  .banner {
    position: absolute; left: 297px; top: 0;
    width: 500px; height: 1200px;
    background: var(--white);
    overflow: hidden;
  }
  .banner-art { position: absolute; inset: 0; width: 500px; height: 1200px; }

  .brand-name {
    position: absolute; top: 50px; left: 0; width: 100%;
    text-align: center;
    font-weight: 800; font-size: 68px; line-height: 80px; letter-spacing: 1px;
    color: var(--green);
  }

  .tagline {
    position: absolute; left: 49px; top: 492px;
    font-weight: 700; font-size: 32px; line-height: 41px;
    color: var(--green); letter-spacing: 0.5px;
    text-transform: uppercase;
  }

  .benefits { list-style: none; }
  .benefit {
    position: absolute; left: 38px; height: 38px;
    display: flex; align-items: center;
    font-weight: 500; font-size: 24px; line-height: 22px;
    color: var(--ink); letter-spacing: 0.3px;
    white-space: nowrap;
  }
  .benefit-secure { top: 626px; }
  .benefit-mobile { top: 679px; }
  .benefit-easy { top: 730px; }
  .benefit-quick { top: 771px; }
  .benefit-icon { width: 38px; height: 38px; flex: none; margin-right: 18px; }

  .modules-tag {
    position: absolute; left: 42px; top: 835px;
    width: 206px; height: 30px;
    background: var(--green);
    transform: skewX(-8deg);
  }
  .modules-tag span {
    display: block; transform: skewX(8deg);
    color: var(--white); font-weight: 600; font-size: 19px;
    line-height: 30px; text-align: center;
  }

  .module { position: absolute; left: 43px; width: 290px; }
  .module-name { color: var(--red); font-weight: 700; font-size: 18px; line-height: 19.5px; }
  .module-desc { color: var(--ink); font-weight: 400; font-size: 17px; line-height: 19.5px; }
  .module-one { top: 877px; }
  .module-two { top: 943px; }

  .site-url {
    position: absolute; left: 45px; top: 1103px;
    color: var(--white); font-weight: 700; font-size: 31px; line-height: 38px; letter-spacing: 0.3px;
  }
</style>
</head>
<body>
<main class="banner">
  <svg class="banner-art" viewBox="0 0 500 1200" xmlns="http://www.w3.org/2000/svg">
    <defs>
      <linearGradient id="heroTone" x1="0" y1="0" x2="1" y2="1">
        <stop offset="0" stop-color="#8a6a55"/>
        <stop offset="0.35" stop-color="#8c9aa3"/>
        <stop offset="0.7" stop-color="#3c4a52"/>
        <stop offset="1" stop-color="#d8dde0"/>
      </linearGradient>
      <radialGradient id="circleTone" cx="0.55" cy="0.45" r="0.6">
        <stop offset="0" stop-color="#cfe6ee"/>
        <stop offset="0.6" stop-color="#5d7f92"/>
        <stop offset="1" stop-color="#24394a"/>
      </radialGradient>
      <linearGradient id="footTone" x1="0" y1="0" x2="0" y2="1">
        <stop offset="0" stop-color="#1b6f35"/>
        <stop offset="1" stop-color="#12973f"/>
      </linearGradient>
    </defs>

    <path d="M0,404 Q250,517 500,445" fill="none" stroke="var(--red)" stroke-width="14"/>
    <path d="M0,390 Q250,501 500,434" fill="none" stroke="var(--green)" stroke-width="12"/>
    <g role="img" aria-label="Photo of hands at a laptop with a cloud software diagram linking database, network, PC, app server, code and mobile">
      <path d="M0,188 Q250,104 500,188 L500,432 Q250,497 0,386 Z" fill="url(#heroTone)"/>
    </g>
    <path d="M0,190 Q250,106 500,190" fill="none" stroke="var(--green)" stroke-width="8"/>

    <path d="M0,1040 Q250,1120 500,1012" fill="none" stroke="var(--red)" stroke-width="12"/>
    <path d="M0,1046 Q250,1126 500,1018 L500,1200 L0,1200 Z" fill="url(#footTone)"/>

    <g role="img" aria-label="Photo of a hand touching a digital interface diagram">
      <circle cx="399" cy="1020" r="84" fill="url(#circleTone)"/>
    </g>
    <circle cx="399" cy="1020" r="84" fill="none" stroke="var(--red)" stroke-width="4"/>
  </svg>

  <div class="brand-name">VERITAL</div>

  <h1 class="tagline">Patient Safety<br>Solutions for<br>Every Hospital</h1>

  <ul class="benefits">
    <li class="benefit benefit-secure">
      <svg class="benefit-icon" viewBox="0 0 40 40"><circle cx="20" cy="20" r="19" fill="var(--red)"/><path d="M12,24 a5,5 0 0 1 1-10 a7,7 0 0 1 13-1 a5,5 0 0 1 2,11 Z" fill="none" stroke="#fff" stroke-width="1.8"/><path d="M20,24 v5 M15,24 v4 M25,24 v4" stroke="#fff" stroke-width="1.8"/></svg>
      Secure Saas Solution
    </li>
    <li class="benefit benefit-mobile">
      <svg class="benefit-icon" viewBox="0 0 40 40"><circle cx="20" cy="20" r="19" fill="var(--red)"/><rect x="10" y="12" width="17" height="12" fill="none" stroke="#fff" stroke-width="1.8"/><path d="M15,28 h7 M18.5,24 v4" stroke="#fff" stroke-width="1.8"/><rect x="25" y="18" width="6" height="11" rx="1" fill="var(--red)" stroke="#fff" stroke-width="1.8"/></svg>
      <span>Modern and<br>Mobile responsive</span>
    </li>
    <li class="benefit benefit-easy">
      <svg class="benefit-icon" viewBox="0 0 40 40"><circle cx="20" cy="20" r="19" fill="var(--red)"/><path d="M17,21 V11 a2,2 0 0 1 4,0 V19 l5,1 a2,2 0 0 1 2,2 v4 a5,5 0 0 1 -5,5 h-3 a4,4 0 0 1 -3,-1.5 L12,24 a1.8,1.8 0 0 1 3,-2 Z" fill="none" stroke="#fff" stroke-width="1.8" stroke-linejoin="round"/></svg>
      Easy to use
    </li>
    <li class="benefit benefit-quick">
      <svg class="benefit-icon" viewBox="0 0 40 40"><circle cx="20" cy="20" r="19" fill="var(--red)"/><path d="M23,8 L13,22 h7 l-3,10 L27,18 h-7 Z" fill="none" stroke="#fff" stroke-width="1.8" stroke-linejoin="round"/></svg>
      Quick to deploy
    </li>
  </ul>

  <div class="modules-tag"><span>Flagship Modules</span></div>

  <section class="module module-one">
    <h2 class="module-name">Beacon Desk</h2>
    <p class="module-desc">Make Incident reporting easy,<br>meaningful and secure.</p>
  </section>
  <section class="module module-two">
    <h2 class="module-name">Larkspur Summit<br>Console</h2>
    <p class="module-desc">Driver quality improvement<br>efforts in healthcare.</p>
  </section>

  <div class="site-url">www.carewardhq.com</div>
</main>
</body>
</html>
```